Progressive/contemporary business card design for successful Startups as a Service Company

New logo launched in 2020. New website launched in 2021. Now that COVID is (mostly) behind us, I'm networking with more people and need a business card that matches the company/logo design aesthetic.

```html
<!DOCTYPE html>
<html lang="en">
<head>
<meta charset="utf-8">
<title>Launchwise – Business Card</title>
<link href="https://fonts.googleapis.com/css2?family=Montserrat:wght@400&family=Arimo:wght@400;700&display=swap" rel="stylesheet">
<style>
  :root {
    --backdrop: #1d1d1f;
    --card: #0a0a0b;
    --brand-slate: #5b6c88;
    --text-light: #d9dbe0;
    --divider: #2a2b2f;
  }
  html, body {
    margin: 0;
    padding: 0;
    width: 1200px;
    height: 900px;
    overflow: hidden;
    background: var(--backdrop);
  }
  .canvas {
    position: relative;
    width: 1200px;
    height: 900px;
  }
  .card {
    position: absolute;
    left: 260px;
    width: 680px;
    height: 388px;
    background: var(--card);
    box-shadow: 0 14px 34px rgba(0,0,0,0.55);
  }
  .card--back { top: 48px; }
  .card--front { top: 464px; }

  .wordmark {
    display: flex;
    align-items: center;
    gap: 14px;
    font-family: "Montserrat", sans-serif;
    font-weight: 400;
    color: var(--brand-slate);
    letter-spacing: 0.22em;
    white-space: nowrap;
  }
  .wordmark__square {
    width: 16px;
    height: 16px;
    background: var(--brand-slate);
  }
  .card--back .wordmark {
    position: absolute;
    left: 50%;
    top: 50%;
    transform: translate(-50%, -50%);
    font-size: 40px;
  }
  .card--front .wordmark {
    position: absolute;
    left: 60px;
    top: 50%;
    transform: translateY(-50%);
    font-size: 30px;
  }

  .card__divider {
    position: absolute;
    left: 372px;
    top: 80px;
    width: 1px;
    height: 228px;
    background: var(--divider);
  }

  .contact {
    position: absolute;
    left: 402px;
    top: 86px;
    font-family: "Arimo", sans-serif;
    color: var(--text-light);
  }
  .contact__name {
    margin: 0;
    font-size: 23px;
    font-weight: 700;
    color: var(--brand-slate);
    letter-spacing: 0.02em;
    text-transform: uppercase;
  }
  .contact__role {
    margin: 2px 0 14px;
    font-size: 16px;
  }
  .contact__list {
    list-style: none;
    margin: 0 0 18px;
    padding: 0;
  }
  .contact__item {
    display: flex;
    align-items: center;
    gap: 8px;
    font-size: 15px;
    line-height: 24px;
  }
  .contact__icon {
    width: 14px;
    height: 14px;
    flex: none;
  }
  .contact__address {
    margin: 0;
    padding-left: 22px;
    font-size: 15px;
    line-height: 21px;
    font-style: normal;
  }
</style>
</head>
<body>
<main class="canvas">

  <section class="card card--back" aria-label="Business card back">
    <div class="wordmark">LAUNCHWISE<span class="wordmark__square"></span></div>
  </section>

  <section class="card card--front" aria-label="Business card front">
    <div class="wordmark">LAUNCHWISE<span class="wordmark__square"></span></div>
    <div class="card__divider"></div>

    <div class="contact">
      <h1 class="contact__name">Daniel Reyes</h1>
      <p class="contact__role">Managing Director</p>
      <ul class="contact__list">
        <li class="contact__item">
          <svg class="contact__icon" viewBox="0 0 16 16" aria-hidden="true">
            <path d="M3.5 1.5l2.3 0 1 3.2-1.5 1.2a8 8 0 0 0 4.8 4.8l1.2-1.5 3.2 1v2.3c0 .8-.7 1.5-1.5 1.5A12.5 12.5 0 0 1 2 3c0-.8.7-1.5 1.5-1.5z" fill="var(--text-light)"/>
          </svg>
          044-555 018 240
        </li>
        <li class="contact__item">
          <svg class="contact__icon" viewBox="0 0 16 16" aria-hidden="true">
            <rect x="1" y="3" width="14" height="10" fill="var(--text-light)"/>
            <path d="M1 3l7 6 7-6" fill="none" stroke="var(--card)" stroke-width="1.3"/>
          </svg>
          hello@launchwise.co
        </li>
        <li class="contact__item">
          <svg class="contact__icon" viewBox="0 0 16 16" aria-hidden="true">
            <g fill="none" stroke="var(--text-light)" stroke-width="1.2">
              <circle cx="8" cy="8" r="6.5"/>
              <ellipse cx="8" cy="8" rx="3" ry="6.5"/>
              <path d="M1.5 8h13M2.5 4.8h11M2.5 11.2h11"/>
            </g>
          </svg>
          www.launchwise.co
        </li>
      </ul>
      <address class="contact__address">88 Harbor Street, Suite 4<br>10233, Westland</address>
    </div>
  </section>

</main>
</body>
</html>
```